Wine Label Design for Marrick Estate

I need a front and back label for a new wine I am making. I am looking for a classic, elegant and serious wine label. I would like the label to be white with blue and black writing. The blue will be the distinction in the label. The color of blue will be unique and catch the eye. The font of the writing will be unique and could also serve as the brand image for Marrick Estate. The label can have a design but should be simple and distinct. I envision the paper quality of the label to textured, high quality and add to the overall image of the label.
The label will be timeless. The price of this wine will be $85.00 a bottle, and the label should match a higher priced wine. This wine is family owned and operated.
The writing on the front and back label will be:

FRONT Label-

Marrick Estate

Howell Mountain

Napa Valley

2022 Cabernet Sauvignon

Back Label-

Cellared and Bottled by Marrick Estate, Angwin, CA 94508

GOVERNMENT WARNING: (1) According to the Surgeon General, women should not drink alcoholic beverages during pregnancy because of the risk of birth defects. (2) Consumption of alcoholic beverages impairs your ability to drive a car or operate machinery, and may cause health problems.

Alc. 14.5% by Vol.

750 ml

Contains Sulfites

```html
<!DOCTYPE html>
<html lang="en">
<head>
<meta charset="utf-8">
<title>Marrick Estate – Front Label</title>
<link rel="stylesheet" href="https://fonts.googleapis.com/css2?family=Cormorant+Garamond:wght@500;600&family=Monsieur+La+Doulaise&display=swap">
<style>
  :root {
    --page: #ffffff;
    --paper: #ffffff;
    --frame: #9a9a9a;
    --ink: #141414;
    --estate-blue: #1f1fe6;
    --leaf-grey: #e4e4e4;
  }
  * { box-sizing: border-box; margin: 0; padding: 0; }
  html, body {
    width: 1200px;
    height: 1200px;
    overflow: hidden;
    background: var(--page);
  }
  .canvas {
    position: relative;
    width: 1200px;
    height: 1200px;
  }
  .front-label {
    position: absolute;
    left: 226px;
    top: 80px;
    width: 749px;
    height: 1040px;
    background: var(--paper);
    border: 1.5px solid var(--frame);
    overflow: hidden;
  }
  .vine-leaf {
    position: absolute;
    left: 135px;
    top: 24px;
    width: 575px;
    height: 625px;
    border-radius: 46% 40% 44% 50%;
    background: linear-gradient(135deg,
      var(--leaf-grey) 0%,
      #eeeeee 48%,
      #c9c9f5 62%,
      var(--estate-blue) 100%);
    opacity: 0.9;
  }
  .vine-tendril {
    position: absolute;
    left: 0;
    top: 330px;
    width: 220px;
    height: 120px;
  }
  .brand-name {
    position: absolute;
    left: 0;
    top: 60px;
    width: 100%;
    text-align: center;
    font-family: "Monsieur La Doulaise", cursive;
    font-weight: 400;
    color: var(--ink);
    line-height: 0.95;
  }
  .brand-name__first {
    display: block;
    font-size: 210px;
    transform: translateX(-20px);
  }
  .brand-name__second {
    display: block;
    font-size: 190px;
    transform: translateX(-40px);
    margin-top: -10px;
  }
  .appellation {
    position: absolute;
    left: 0;
    top: 665px;
    width: 100%;
    text-align: center;
    font-family: "Cormorant Garamond", serif;
    font-weight: 500;
    font-size: 38px;
    line-height: 44px;
    letter-spacing: 0.22em;
    text-transform: uppercase;
    color: var(--ink);
  }
  .vintage {
    position: absolute;
    left: 0;
    top: 818px;
    width: 100%;
    text-align: center;
    font-family: "Cormorant Garamond", serif;
    font-weight: 600;
    font-size: 66px;
    letter-spacing: 0.02em;
    color: var(--ink);
  }
  .varietal {
    position: absolute;
    left: 0;
    top: 918px;
    width: 100%;
    text-align: center;
    font-family: "Cormorant Garamond", serif;
    font-weight: 600;
    font-size: 36px;
    letter-spacing: 0.04em;
    text-transform: uppercase;
    color: var(--ink);
  }
</style>
</head>
<body>
  <main class="canvas">
    <section class="front-label">
      <div class="vine-leaf" role="img" aria-label="Engraved grape leaf illustration in light grey fading into vivid blue along its lower right edge"></div>
      <svg class="vine-tendril" viewBox="0 0 220 120" aria-hidden="true">
        <path d="M0 20 C40 70 120 110 220 60" fill="none" stroke="#d8d8d8" stroke-width="5" stroke-linecap="round"/>
      </svg>
      <h1 class="brand-name">
        <span class="brand-name__first">Marrick</span>
        <span class="brand-name__second">Estate</span>
      </h1>
      <p class="appellation">Howell Mountain<br>Napa Valley</p>
      <p class="vintage">2022</p>
      <p class="varietal">Cabernet Sauvignon</p>
    </section>
  </main>
</body>
</html>
```